DESIGN AD FOR QUILLBRIEF MAGAZINE

Improve upon attached existing draft Ad for a lawyer magazine.

We are promoting our Online print management system to Lawyers.

You have the abilty to be creative and offer something different if you prefer.

The attached pdf has two draft examples.

Full-page bleed 8.625 x 11.125
Trim Size 8.375 x 10.875
PDF-A CMYK high-res 300 dpi same-size file is required. Embed all Fonts and graphics in file. Do not set trap.

Target Market(s)

Lawyers

Industry/Entity Type

Legal

Font styles to use
Sans Serif

Requirements
Must have
• Full-page bleed 8.625 x 11.125
• Trim Size 8.375 x 10.875
• PDF-A CMYK high-res 300 dpi same-size file is required. Embed all Fonts and graphics in file. Do not set trap.
Nice to have
• Here is some information about the Legal Segment ( BACKGROUND INFORMATION ONLY).
• Digital print plays an important role in accommodating the needs of the legal industry, as it offers the features that address the operations and marketing sides of firms. Legal firms take advantage of the benefits of digital printing—short run, high-quality, personalization, fast turnaround, just-in-time, efficient production—to support the litigation process, manage regulatory compliance and generate profits.
• The law business is a relationship business. It is imperative for firms in the legal industry to consistently and persistently cultivate, nurture and strengthen their relationships with current clients to receive more work, with referral sources to receive more referrals and with prospects to develop new work. However, legal services firms don’t have a system in place (formal or otherwise) for getting and staying in touch with clients and prospects. A common phrase in the marketing world is that it takes from 7–10 "touches" annually to stay "top-of-mind" of customers and prospects. This means regular, consistent and persistent "touchpoints," via direct mail, email, newsletters, phone calls, face-to-face, social media outlets and more.
• Legal firms need to continually build their reputation and strengthen relationships, which presents an opportunity for digital printing. Key touchpoints include direct mail, printed newsletters, postcards, coupons, remainder notices and more. Given that many firms in the legal industry are small-size firms, digitally printing these materials is a viable option. Also, using variable data printing to customize these touchpoints increases their effectiveness.
• Digital printing’s ability to produce short runs in short turnaround times enables just-in-time, on-demand production. The cost savings of on-demand production can be significant.
• Digital printing allows for economically adding color to a wider range of branded communications and enhancing the image they portray.
• And you can take advantage of high-value digital printing solutions to implement cross-media and 1:1 marketing programs…the key to growing revenue.
• Digital printing offers many advantages:
• Strengthen relationships with targeted, customized communication
• Produce materials on-demand and in quantities needed
• Build reputation and relationships by providing customized information for customers and prospects on services, capabilities, and strengths
• Create 1-to-1 relationships with the customers where they perceive they are receiving additional value
• Using variable information and color in communications increases readability and retention, driving down the costs for customer support
• Examples of key applications, a number of which we are going to discuss, include:
• Brochures
• Business Cards
• Direct Mail
• Directories
• Marketing Materials
• Postcards
• Trial Boards

```html
<!DOCTYPE html>
<html lang="en">
<head>
<meta charset="utf-8">
<title>Meridian PSG – Online Print Management Ad</title>
<link rel="stylesheet" href="https://fonts.googleapis.com/css2?family=Jost:wght@300;400;500;700;800&family=Barlow+Condensed:wght@600;700&family=Montserrat:wght@700;800&display=swap">
<style>
  :root {
    --page-bg: #d9dadc;
    --paper: #ffffff;
    --blue: #2a8bc0;
    --blue-deep: #1a6fae;
    --green: #4f9e6a;
    --green-band: #5ba872;
    --chip: #7fcbe2;
    --ink: #1e1e1e;
    --ink-soft: #333333;
  }
  * { box-sizing: border-box; margin: 0; padding: 0; }
  html, body { width: 1194px; height: 1200px; overflow: hidden; }
  body { background: var(--page-bg); position: relative; font-family: "Jost", sans-serif; color: var(--ink); }

  .ad {
    position: absolute; left: 133px; top: 2px; width: 928px; height: 1196px;
    background: var(--paper); border: 1px solid #9a9a9a; overflow: hidden;
  }
  .abs { position: absolute; }

  .site-url { left: 57px; top: 56px; font: 700 19px "Montserrat", sans-serif; letter-spacing: .2px; }
  .ribbon { left: 0; top: 100px; width: 298px; height: 38px; }
  .ribbon-text { left: 56px; top: 101px; font: 700 27px/36px "Barlow Condensed", sans-serif; color: #fff; letter-spacing: .3px; }

  .brand-name { right: 62px; top: 52px; font: 800 82px/1 "Jost", sans-serif; color: var(--blue); letter-spacing: -1px; }
  .brand-tagline { right: 62px; top: 148px; font: 700 19px "Montserrat", sans-serif; color: var(--ink-soft); }

  .hero-photo {
    left: 59px; top: 192px; width: 809px; height: 302px;
    background: linear-gradient(100deg, #0e1a2e 0%, #1d3a66 22%, #dfe9f6 45%, #f4f7fb 62%, #bcd2ee 80%, #e9eef7 100%);
  }

  .headline { left: 50px; top: 505px; font: 800 78px/68px "Jost", sans-serif; color: var(--blue); text-transform: uppercase; letter-spacing: -1px; }

  .screen-visual {
    left: 392px; top: 636px; width: 478px; height: 450px;
    background: linear-gradient(180deg, #2a2a2e 0%, #3b6fa6 12%, #e9f1f8 40%, #ffffff 68%, #c9ccd1 82%, #eceef1 100%);
    border-radius: 10px;
  }

  .subhead { left: 52px; top: 736px; font: 700 28px/27px "Barlow Condensed", sans-serif; color: var(--green); text-transform: uppercase; }

  .chip { position: absolute; height: 23px; background: var(--chip); color: #fff; font: 700 20px/23px "Barlow Condensed", sans-serif; padding-left: 10px; text-transform: uppercase; white-space: nowrap; }

  .local { left: 43px; top: 931px; font: 700 21px/20px "Barlow Condensed", sans-serif; color: var(--blue-deep); text-transform: uppercase; letter-spacing: .3px; }
  .side-band { left: 0; top: 978px; width: 32px; height: 92px; background: var(--green-band); }

  .benefits { left: 43px; top: 976px; font-size: 15px; line-height: 19px; font-weight: 400; }
  .benefits h3 { font: 700 15px/19px "Jost", sans-serif; text-transform: uppercase; }
  .benefits ul { list-style: none; }

  .rule { left: 45px; top: 1084px; width: 350px; height: 1px; background: var(--green); }

  .pledge { left: 45px; top: 1092px; width: 370px; }
  .pledge h4 { font: 300 19px/22px "Jost", sans-serif; text-transform: uppercase; }
  .pledge p { font: 400 11.3px/15px "Jost", sans-serif; margin-top: 3px; }

  .call-bar { left: 425px; top: 1115px; width: 503px; height: 39px; background: var(--blue-deep); color: #fff; font: 700 28px/39px "Jost", sans-serif; text-align: center; letter-spacing: .3px; }
</style>
</head>
<body>
  <main class="ad">
    <div class="abs site-url">www.meridianpsg.com/qbf</div>
    <svg class="abs ribbon" viewBox="0 0 298 38" aria-hidden="true"><polygon points="0,0 298,0 270,19 298,38 0,38" fill="var(--green-band)"/></svg>
    <div class="abs ribbon-text">FREE SITE SETUP</div>

    <div class="abs brand-name">MERIDIAN</div>
    <div class="abs brand-tagline">print. signs. graphics.</div>

    <div class="abs hero-photo" role="img" aria-label="Photo of hands passing a pen and a printed legal document across a desk"></div>

    <h1 class="abs headline">Customized Online<br>Print Management<br>System</h1>

    <div class="abs screen-visual" role="img" aria-label="Desktop monitor showing the online client portal with order history and firm storefronts"></div>

    <h2 class="abs subhead">Leave the printing<br>to the professionals</h2>

    <div class="chip" style="left:40px;top:800px;width:313px">Business Cards &amp; Letterhead</div>
    <div class="chip" style="left:40px;top:827px;width:132px">Direct Mail</div>
    <div class="chip" style="left:178px;top:827px;width:120px">Brochures</div>
    <div class="chip" style="left:40px;top:855px;width:132px">Prospectus</div>
    <div class="chip" style="left:178px;top:855px;width:210px">Legal Copy Services</div>
    <div class="chip" style="left:40px;top:882px;width:233px">Courtroom Graphics</div>

    <div class="abs local">Locally owned &amp;<br>operated since 1999</div>
    <div class="abs side-band"></div>

    <section class="abs benefits">
      <h3>Benefits</h3>
      <ul>
        <li>• Brand Consistency • Cost Savings • Short Run</li>
        <li>• Fast Turnaround Pickup &amp; Delivery</li>
        <li>• Instant Quotes • Affordable Color • Simple Workflow</li>
        <li>• High-Value Solutions • 1:1 Marketing</li>
      </ul>
    </section>

    <div class="abs rule"></div>

    <section class="abs pledge">
      <h4>Bend over backwards</h4>
      <p>At Meridian PSG, we will do whatever it takes to ensure your job prints exactly how you want and is delivered when you want it. That’s our commitment to delivering the highest standard of service in the industry</p>
    </section>

    <div class="abs call-bar">Call Today: 555.014.2290</div>
  </main>
</body>
</html>
```